Photography Company Seeks Amazing and Fun Website Design

Note: This is for design only. No coding required. We want to see your ideas for a great website! This will be a FUN design and not boring like others you may work on.

Please let your creative ideas flow. We have given you a ton of info along with videos to help you understand what we are after, however we WANT your creativity to shine through in your designs!

We are a professional company that has run hundreds of crowdsourced projects on multiple platforms. If you participate in this contest (we hope you do) you can expect great video feedback, consistent feedback, and also our guarantee that if we know your website design will not be what we are looking for we will notify you so you don’t waste your time if there is no chance of you winning.

We respect and recognize this is how you make your living and we will not play games. We look forward to an awesome contest and awesome website designs.

Design Brief:

We are looking for a stunning website design to showcase this amazing photography company. Their current site is:

http://www.kelvaprints.example/

As you can see they do amazing photography and need an amazing website to showcase their work and to attract new people into their studios.

We are looking to get a website that is clean, classy, bright, artistic, and that really helps this company stand out amongst other photography companies.

We need a homepage and an interior page mockup.

Here are some examples of other sites in their business with what we like:

http://www.tabrowenstudio.example/

Please watch video to learn what we like and don’t like:http://clipvault.example/t/QpR4sz7LmWd

http://www.holbrinkimaging.example/

Please watch video to learn what we like and don’t like: http://clipvault.example/t/Hb8ufN2kxyPa

NOTE: We do not want to copy anything outright. We want to learn, model and take their ideas and make them better. We also want to be flexible and take what we like along with your creativity to make an amazing design.

Here is what we are looking for in more specific terms:

NOTE: Website should have a spot for video on the homepage.

This website is for a very professional and well know photography company. Because it is photography the website needs to be VERY visual.

Site should be unique and really stand out to help sell the business and their services. EVERYTHING about this business is visual, so the site MUST reflect that.

Site Overall: Fun and Artistic. This is a forward thinking company that is fun, upbeat, and does things differently, they need the design to reflect that. This is a modern photography company.

They also do all kinds of photography from school kids, sports teams, in studio shoots with High School Seniors, Family Pictures etc.

Colors: We like the white background because it is clean and really helps the photos stand out. Also please look at the logo too. Use colors from that and make things flow. Again we want this to stand out and be different while at the same time being clean.

Menu: Horizontal. We like bold and easy to read menu items. Don’t make it small and cluttered. Include the same items that are in the other site for the mock up.

Site Structure: Clean and easy to navigate. We have a lot of content to display so we need a clean structure that breaks up the text and content areas.

Images: Please pull images from the current site. We can always replace the images of course, but if you show them “their own stuff” in the new design you will be closer to winning because it will feel more like “them”

Content Areas: It is a safe bet that if it is on the current site we need it on the new site. So don’t drop anything as it makes it hard to “cut content”.

What we don't want: We do not want clutter, boring, or templates or themes. We don’t want too cartoony, too cute, or too fancy. We don’t want ugly.

Out of respect to professional designers who really are working hard to win if you do not follow this brief, you submit worn out themes, templates, or boring designs you will be eliminated. We are offering great prize money for this so we expect great visual designs.

Thanks,

The Solvane Team

Target Market(s)

Target Market are upper middle class who want a better photography studio then the average studio, but don't want to go to the highest end of photography. This studio will cater to higher middle class.

Industry/Entity Type

Business

Number of Pages Required

1 page

Font styles to use
Sans Serif

Requirements
Must have
• Video on Home page
• Clean
• Stand Out
• Fun
• Professional
Nice to have
• Creative
• Lots of content in a great structure
Should not have
• clutter
• ugly design
• messy

```html
<!DOCTYPE html>
<html lang="en">
<head>
<meta charset="utf-8">
<title>Kelva Photography</title>
<link href="https://fonts.googleapis.com/css2?family=Dosis:wght@400;500;600;700&family=Open+Sans:wght@400;600;700&display=swap" rel="stylesheet">
<style>
:root{
  --teal:#2aa7a4;
  --teal-soft:#55bdb9;
  --magenta:#b3408f;
  --pink-line:#e6b1d3;
  --ink:#333;
  --muted:#888;
  --rule:#d9d9d9;
  --nav:#ececec;
  --footer:#474747;
  --footer-dark:#3a3a3a;
  --white:#fff;
}
*{box-sizing:border-box;margin:0;padding:0}
html,body{width:1200px;height:3750px;overflow:hidden}
body{background:var(--white);font-family:"Open Sans",sans-serif;color:var(--ink);position:relative}
a{color:inherit;text-decoration:none}

/* header */
.site-header{height:112px;display:flex;align-items:center;justify-content:center;gap:12px}
.brand-dot{width:20px;height:20px;border-radius:50%;background:var(--teal)}
.brand-name{font-family:"Dosis",sans-serif;font-weight:600;font-size:44px;color:#222;letter-spacing:1px}
.main-nav{background:var(--nav);height:40px;display:flex;justify-content:center;align-items:center;gap:6px}
.main-nav a{font-family:"Dosis",sans-serif;font-weight:600;font-size:12px;letter-spacing:1px;color:#555;padding:6px 14px}
.main-nav a.active{background:#fff;color:var(--teal)}

/* hero */
.hero{position:absolute;top:172px;left:162px;width:876px;height:413px;overflow:hidden}
.hero-photo{position:absolute;inset:0;background:linear-gradient(100deg,#6e6e6e 0%,#a4a4a4 40%,#d8d8d8 70%,#ececec 100%)}
.hero-welcome{position:absolute;left:560px;top:128px;font-family:"Dosis",sans-serif;font-size:36px;font-weight:600;color:#333;white-space:nowrap}
.hero-play{position:absolute;left:560px;top:178px;display:flex;align-items:center;gap:12px;font-family:"Dosis",sans-serif;font-size:28px;color:#333}
.hero-cta{position:absolute;left:18px;bottom:18px;font-family:"Dosis",sans-serif;font-weight:600;font-size:30px;color:var(--magenta)}
.hero-dots{position:absolute;right:18px;bottom:22px;display:flex;gap:5px}
.hero-dots i{width:8px;height:8px;border-radius:50%;background:#999}
.hero-dots i.on{background:#333}

/* section titles */
.section-title{position:absolute;left:0;width:1200px;display:flex;justify-content:center;align-items:center;gap:16px;font-family:"Dosis",sans-serif;font-weight:600;font-size:12px;letter-spacing:2px;color:#555;text-transform:uppercase}
.section-title::before,.section-title::after{content:"";width:320px;height:1px;background:var(--rule)}

/* services */
.services{position:absolute;top:652px;left:162px;width:876px;display:flex;justify-content:space-between}
.service-card{width:200px;height:232px;border:1px solid var(--rule);text-align:center;padding:28px 18px 0;background:#fff}
.service-card.featured{border:3px solid var(--pink-line)}
.service-card h3{font-family:"Dosis",sans-serif;font-size:13px;font-weight:700;margin:14px 0 8px;color:#333}
.service-card p{font-size:10.5px;line-height:1.6;color:var(--muted)}
.more-dot{margin:10px auto 0;width:10px;height:10px;border-radius:50%;border:2px solid var(--teal)}

/* work */
.work-head{position:absolute;top:936px;left:162px;width:876px;display:flex;justify-content:space-between;align-items:center;font-family:"Dosis",sans-serif;font-size:12px;font-weight:600;letter-spacing:1.5px;color:#444}
.work-head .filters{display:flex;gap:18px;font-size:10px;color:#666}
.work-head .filters span.on{color:var(--magenta)}
.gallery{position:absolute;top:972px;left:162px;width:876px;height:744px}
.tile{position:absolute}
.tile.feature{background:var(--teal-soft);display:flex;align-items:center;justify-content:center;font-family:"Dosis",sans-serif;color:#fff;font-size:14px;font-weight:600;letter-spacing:1px}

/* together */
.together{position:absolute;top:1766px;width:1200px;text-align:center;font-family:"Dosis",sans-serif;font-size:13px;letter-spacing:1.5px;color:#555}
.together-actions{position:absolute;top:1804px;width:1200px;display:flex;justify-content:center;gap:14px}
.btn{display:inline-block;font-family:"Dosis",sans-serif;font-weight:600;font-size:12px;letter-spacing:1px;color:#fff;padding:9px 26px}
.btn.teal{background:var(--teal)}
.btn.magenta{background:var(--magenta)}

/* bands */
.band{position:absolute;left:0;width:1200px;height:250px}
.band-bg{position:absolute;inset:0;background:radial-gradient(ellipse at 55% 50%,#4a4a4a 0,#7d7d7d 30%,#b0b0b0 65%,#c8c8c8 100%)}
.band-content{position:absolute;inset:0;display:flex;flex-direction:column;align-items:center;justify-content:center;color:#fff;text-align:center}
.band-label{font-family:"Dosis",sans-serif;font-size:12px;letter-spacing:2px;margin-bottom:18px}
.band-text{font-family:"Dosis",sans-serif;font-size:18px;line-height:1.5;width:820px}
.band-link{margin-top:14px;font-family:"Dosis",sans-serif;font-size:11px;color:var(--magenta);letter-spacing:1px}
.band-dots{display:flex;gap:6px;margin-top:16px}
.band-dots i{width:8px;height:8px;border-radius:50%;background:#ddd}
.band-dots i.on{background:#333}

/* pricing */
.pricing{position:absolute;top:2212px;left:162px;width:876px;display:flex;justify-content:space-between}
.price-card{width:200px;height:278px;border:3px solid var(--pink-line);text-align:center;padding-top:20px}
.price-card h3{font-family:"Dosis",sans-serif;font-size:20px;font-weight:500;color:#333}
.price-badge{width:76px;height:76px;border-radius:50%;background:#555;border:5px solid #ddd;margin:14px auto 12px;display:flex;align-items:center;justify-content:center;color:#fff;font-family:"Dosis",sans-serif;font-size:24px;font-weight:600}
.price-badge small{font-size:10px;font-weight:400;margin-left:2px}
.price-card ul{list-style:none;font-size:10px;line-height:1.7;color:#666}
.price-buy{margin-top:10px;display:flex;justify-content:center;align-items:center;gap:4px}
.price-buy span{background:var(--teal);color:#fff;font-family:"Dosis",sans-serif;font-size:13px;padding:5px 16px}
.price-buy span.alt{background:#777}
.browse{position:absolute;top:2533px;width:1200px;text-align:center}

/* specials */
.special{position:absolute;top:2640px;left:356px;width:560px;height:150px}
.special-photo{position:absolute;left:0;top:6px;width:160px;height:140px;background:linear-gradient(135deg,#d9b9a2,#e9d6c6 50%,#b99482)}
.special-seal{position:absolute;left:118px;top:-4px;width:44px;height:44px;border-radius:50%;background:var(--teal-soft);border:3px solid #fff}
.special-body{position:absolute;left:184px;top:0;font-size:11px;line-height:1.65;color:#444}
.special-body h4{font-family:"Dosis",sans-serif;font-size:14px;font-weight:600;color:#222}
.special-body .value{color:var(--magenta);font-weight:700}
.slider-arrow{position:absolute;width:32px;height:32px;border-radius:50%;background:#9a9a9a;display:flex;align-items:center;justify-content:center}
.urgent{position:absolute;top:2826px;width:1200px;text-align:center;font-family:"Dosis",sans-serif;font-size:15px;font-weight:600;letter-spacing:3px;color:var(--teal)}

/* partners */
.partners{position:absolute;top:3204px;left:162px;width:876px;display:flex;justify-content:space-between;align-items:center}
.partner{width:78px;height:78px}

/* footer */
.site-footer{position:absolute;top:3328px;left:0;width:1200px;height:368px;background:var(--footer);color:#ccc}
.footer-links{position:absolute;left:162px;top:88px;list-style:none;font-family:"Dosis",sans-serif;font-size:11px;line-height:1.55}
.footer-links li:first-child{color:var(--teal)}
.footer-contact{position:absolute;left:350px;top:70px;width:500px;text-align:center;font-size:10.5px;line-height:1.6}
.footer-contact h5,.footer-about h5{font-family:"Dosis",sans-serif;font-size:13px;font-weight:700;color:#fff;letter-spacing:1px;margin-bottom:10px}
.social{display:flex;justify-content:center;gap:10px;margin:16px 0}
.social i{width:26px;height:26px;border-radius:50%;background:#5d5d5d;border:2px solid var(--magenta)}
.newsletter{display:flex;justify-content:center;margin-top:14px}
.newsletter span{background:#222;color:#aaa;font-size:11px;padding:6px 12px;width:220px;text-align:left}
.newsletter b{background:var(--teal);color:#fff;font-size:11px;padding:6px 12px}
.footer-about{position:absolute;left:903px;top:70px;width:140px;font-size:10px;line-height:1.6}
.copyright{position:absolute;top:3696px;left:0;width:1200px;height:54px;background:var(--footer-dark);color:#aaa;font-size:11px;display:flex;align-items:center;justify-content:center}
</style>
</head>
<body>

<header class="site-header">
  <span class="brand-dot"></span>
  <span class="brand-name">Kelva</span>
</header>
<nav class="main-nav">
  <a class="active">HOME</a><a>STUDIO</a><a>SUPER SENIOR DAYS</a><a>BOOK IT</a><a>VIEWING</a><a>SPORTS</a><a>CONTACT US</a>
</nav>

<section class="hero">
  <div class="hero-photo" role="img" aria-label="Black and white portrait of a photographer holding a camera toward the viewer"></div>
  <div class="hero-welcome">WELCOME TO KELVA !</div>
  <div class="hero-play">PLAY VIDEO
    <svg width="34" height="34" viewBox="0 0 34 34"><circle cx="17" cy="17" r="16" fill="#222"/><path d="M13 10l11 7-11 7z" fill="#fff"/></svg>
  </div>
  <div class="hero-cta">SCHEDULE Your Family Portrait Photo Shoot</div>
  <div class="hero-dots"><i class="on"></i><i></i></div>
</section>

<div class="section-title" style="top:608px">What we do</div>
<section class="services">
  <article class="service-card featured">
    <svg width="46" height="46" viewBox="0 0 46 46"><path d="M4 15 23 7l19 8-19 8z" fill="#2aa7a4"/><rect x="13" y="20" width="20" height="10" fill="#2aa7a4"/><circle cx="23" cy="36" r="6" fill="#2aa7a4"/></svg>
    <h3>SCHOOL PHOTO</h3>
    <p>Bright class portraits taken with care so every student looks their best on picture day.</p>
    <div class="more-dot"></div>
  </article>
  <article class="service-card">
    <svg width="46" height="46" viewBox="0 0 46 46"><path d="M13 6h20v10a10 10 0 0 1-20 0z" fill="#2aa7a4"/><path d="M13 9H6a7 7 0 0 0 7 9M33 9h7a7 7 0 0 1-7 9" stroke="#2aa7a4" stroke-width="3" fill="none"/><rect x="21" y="26" width="4" height="8" fill="#2aa7a4"/><rect x="14" y="34" width="18" height="5" fill="#2aa7a4"/></svg>
    <h3>SPORTS PHOTO</h3>
    <p>Team and action shots for every season, with player cards and banners for the fans.</p>
  </article>
  <article class="service-card">
    <svg width="46" height="46" viewBox="0 0 46 46"><rect x="21" y="3" width="4" height="12" fill="#2aa7a4"/><rect x="17" y="6" width="12" height="3" fill="#2aa7a4"/><path d="M10 24 23 14l13 10v18H10z" fill="#2aa7a4"/><rect x="20" y="32" width="6" height="10" fill="#fff"/></svg>
    <h3>CHURCH PHOTO</h3>
    <p>Directory portraits for your congregation, arranged on site at a time that suits you.</p>
  </article>
  <article class="service-card">
    <svg width="46" height="46" viewBox="0 0 46 46"><circle cx="14" cy="12" r="5" fill="#2aa7a4"/><circle cx="32" cy="12" r="5" fill="#2aa7a4"/><rect x="8" y="19" width="12" height="20" rx="3" fill="#2aa7a4"/><rect x="26" y="19" width="12" height="20" rx="3" fill="#2aa7a4"/><circle cx="23" cy="24" r="3" fill="#2aa7a4"/><rect x="20" y="28" width="6" height="11" rx="2" fill="#2aa7a4"/></svg>
    <h3>FAMILY PHOTO</h3>
    <p>Relaxed family sessions in studio or outdoors, made to hang proudly on your wall.</p>
  </article>
</section>

<div class="work-head">
  <span>— OUR AWESOME WORK</span>
  <div class="filters"><span class="on">ALL</span><span>CONCEPTUAL</span><span>PORTRAIT</span><span>SPORTS</span><span>FAMILY</span></div>
</div>
<section class="gallery">
  <div class="tile" style="left:0;top:0;width:435px;height:290px;background:linear-gradient(135deg,#d8a23a,#b24c3a 45%,#3a5f8a)" role="img" aria-label="Senior portrait in front of a colourful mosaic wall"></div>
  <div class="tile" style="left:441px;top:0;width:216px;height:109px;background:linear-gradient(135deg,#7c6a5a,#a99280)" role="img" aria-label="Large family group portrait"></div>
  <div class="tile" style="left:441px;top:115px;width:216px;height:175px;background:linear-gradient(135deg,#3a3a3a,#6a5445)" role="img" aria-label="Two brothers posing together"></div>
  <div class="tile" style="left:663px;top:0;width:213px;height:290px;background:linear-gradient(160deg,#5a5040,#2a2a2a 60%,#8a6a30)" role="img" aria-label="Football player holding a trophy"></div>
  <div class="tile feature" style="left:0;top:300px;width:213px;height:290px">IMAGE TITLE</div>
  <div class="tile" style="left:0;top:596px;width:213px;height:148px;background:linear-gradient(135deg,#6f8f55,#b9c59a)" role="img" aria-label="Young child with a dog outdoors"></div>
  <div class="tile" style="left:219px;top:300px;width:216px;height:195px;background:linear-gradient(135deg,#4a4a4a,#8a7664)" role="img" aria-label="Team photo of young players"></div>
  <div class="tile" style="left:441px;top:300px;width:216px;height:195px;background:linear-gradient(135deg,#2a2a2a,#5a4a50)" role="img" aria-label="Family in black outfits"></div>
  <div class="tile" style="left:219px;top:501px;width:438px;height:243px;background:linear-gradient(135deg,#3a2a2e,#b08a90 50%,#e0d6d4)" role="img" aria-label="Baby girl seated beside large name letters"></div>
  <div class="tile" style="left:663px;top:300px;width:213px;height:290px;background:linear-gradient(160deg,#1a1a1a,#5a4a3a 50%,#a07a40)" role="img" aria-label="Football player in helmet, close up"></div>
  <div class="tile" style="left:663px;top:596px;width:213px;height:148px;background:linear-gradient(135deg,#1d2a3a,#8a6a20)" role="img" aria-label="Youth football player in action"></div>
</section>

<div class="together">— LET'S MAKE SOMETHING GREAT TOGETHER —</div>
<div class="together-actions"><a class="btn teal">VIEW MORE WORK</a><a class="btn magenta">GET IN TOUCH</a></div>

<section class="band" style="top:1885px">
  <div class="band-bg" role="img" aria-label="Soft blurred studio backdrop"></div>
  <div class="band-content">
    <div class="band-label">WHO WE ARE</div>
    <p class="band-text">Cras justo odio, dapibus ac facilisis in, egestas eget quam. Maecenas faucibus mollis interdum. Vivamus sagittis lacus vel augue laoreet rutrum faucibus dolor auctor gravida</p>
    <div class="band-link">READ MORE</div>
  </div>
</section>

<div class="section-title" style="top:2158px">Sitting fees</div>
<section class="pricing">
  <article class="price-card">
    <h3>HS Seniors</h3>
    <div class="price-badge">$1.5<small>/hr</small></div>
    <ul><li>75% Off Senior Sessions</li><li>Signature Session - $138</li><li>Full Senior Day - $238</li><li>8 Free wallets</li></ul>
    <div class="price-buy"><span>Buy now</span><svg width="14" height="24"><path d="M0 0l14 12L0 24z" fill="#2aa7a4"/></svg></div>
  </article>
  <article class="price-card">
    <h3>Family Portrait</h3>
    <div class="price-badge">$0.9<small>/hr</small></div>
    <ul><li>30% Off Family Sessions</li><li>Studio Session - $98</li><li>Outdoor Session - $148</li><li>8 Free wallets</li></ul>
    <div class="price-buy"><span>Buy now</span><svg width="14" height="24"><path d="M0 0l14 12L0 24z" fill="#2aa7a4"/></svg></div>
  </article>
  <article class="price-card">
    <h3>Church Event</h3>
    <div class="price-badge">$1.2<small>/hr</small></div>
    <ul><li>20% Off Directory Sessions</li><li>Group Session - $120</li><li>Event Coverage - $260</li><li>8 Free wallets</li></ul>
    <div class="price-buy"><span>Buy now</span><svg width="14" height="24"><path d="M0 0l14 12L0 24z" fill="#2aa7a4"/></svg></div>
  </article>
  <article class="price-card">
    <h3>Team Appointments</h3>
    <div class="price-badge">$1.2<small>/hr</small></div>
    <ul><li>30% Off Team Sessions</li><li>Team Photo - $110</li><li>Player Cards - $160</li><li>8 Free wallets</li></ul>
    <div class="price-buy"><span class="alt">Buy now</span><svg width="14" height="24"><path d="M0 0l14 12L0 24z" fill="#777"/></svg></div>
  </article>
</section>
<div class="browse"><a class="btn magenta" style="padding:10px 34px">BROWSE MORE PACKAGES</a></div>

<div class="section-title" style="top:2605px">Specials</div>
<div class="slider-arrow" style="left:102px;top:2702px"><svg width="12" height="12"><path d="M9 1 3 6l6 5" stroke="#fff" stroke-width="2" fill="none"/></svg></div>
<div class="slider-arrow" style="left:1066px;top:2702px"><svg width="12" height="12"><path d="M3 1l6 5-6 5" stroke="#fff" stroke-width="2" fill="none"/></svg></div>
<section class="special">
  <div class="special-photo" role="img" aria-label="Smiling toddler portrait"></div>
  <div class="special-seal"></div>
  <div class="special-body">
    <h4>Mother Days Family or Children Portraits Special</h4>
    <p>5 Minutes</p>
    <p>Family or Children Session / $88 Value</p>
    <p>One 8x10 / $88 Value</p>
    <p>One 5x7 / $79 Value</p>
    <p>One Digital File with unlimited Copyright privileges / $138 Value</p>
    <p class="value">A $387 VALUE FOR ONLY $38</p>
  </div>
</section>
<div class="urgent">LIMITED AVAILABILITY!&nbsp;&nbsp;|&nbsp;&nbsp;CALL TODAY 888-8888</div>

<section class="band" style="top:2870px">
  <div class="band-bg" role="img" aria-label="Soft blurred studio backdrop"></div>
  <div class="band-content">
    <div class="band-label">WHAT OUR CUSTOMERS THINK</div>
    <p class="band-text">Cras justo odio, dapibus ac facilisis in, egestas eget quam. Maecenas faucibus mollis interdum. Vivamus sagittis lacus vel augue laoreet rutrum faucibus dolor auctor gravida</p>
    <div class="band-link">JOHN DOE</div>
    <div class="band-dots"><i class="on"></i><i></i><i></i></div>
  </div>
</section>

<div class="section-title" style="top:3158px">Our partners</div>
<div class="slider-arrow" style="left:96px;top:3230px"><svg width="12" height="12"><path d="M9 1 3 6l6 5" stroke="#fff" stroke-width="2" fill="none"/></svg></div>
<div class="slider-arrow" style="left:1072px;top:3230px"><svg width="12" height="12"><path d="M3 1l6 5-6 5" stroke="#fff" stroke-width="2" fill="none"/></svg></div>
<section class="partners">
  <svg class="partner" viewBox="0 0 78 78"><circle cx="39" cy="39" r="32" fill="#3f7fb0"/></svg>
  <svg class="partner" viewBox="0 0 78 78"><rect x="6" y="18" width="66" height="42" rx="6" fill="#c85a2a"/></svg>
  <svg class="partner" viewBox="0 0 78 78"><rect x="8" y="20" width="62" height="38" fill="#1f3a6b"/></svg>
  <svg class="partner" viewBox="0 0 78 78"><circle cx="39" cy="39" r="30" fill="#555"/></svg>
  <svg class="partner" viewBox="0 0 78 78"><rect x="16" y="12" width="46" height="54" rx="6" fill="#2b5aa8"/></svg>
  <svg class="partner" viewBox="0 0 78 78"><rect x="8" y="18" width="62" height="42" rx="20" fill="#3d7a3a"/></svg>
  <svg class="partner" viewBox="0 0 78 78"><rect x="14" y="14" width="50" height="50" fill="#2c3f7a"/></svg>
  <svg class="partner" viewBox="0 0 78 78"><rect x="6" y="22" width="66" height="34" rx="4" fill="#2e6a3a"/></svg>
</section>

<footer class="site-footer">
  <ul class="footer-links">
    <li>HOME</li><li>CONTACT US</li><li>BOOK IT</li><li>ORDERING</li><li>SUPER SENIOR DAYS</li><li>PRINTS &amp; FRAMES</li><li>CLASS OF 2015 INFO</li><li>SPORTS</li><li>SPECIALS</li><li>STUDIO</li><li>SITTING FEES</li>
  </ul>
  <div class="footer-contact">
    <h5>GET IN TOUCH WITH US</h5>
    <p>Maecenas faucibus mollis interdum. Cras mattis consectetur purus sit amet fermentum. Nullam quis risus eget urna mollis ornare vel eu leo. Donec id elit non mi porta gravida at eget metus.</p>
    <div class="social"><i></i><i></i><i></i><i></i></div>
    <p>2100 Larkspur Avenue, Fernvale&nbsp;&nbsp;|&nbsp;&nbsp;(555) 014-2276&nbsp;&nbsp;|&nbsp;&nbsp;hello@kelvaprints.example</p>
    <div class="newsletter"><span>Enter your Email</span><b>GO</b></div>
  </div>
  <div class="footer-about">
    <h5>ABOUT US</h5>
    <p>Vestibulum id ligula porta felis euismod semper. Duis mollis, est non commodo luctus, nisi erat porttitor ligula, eget lacinia odio sem nec elit.</p>
    <p style="margin-top:8px">Etiam porta sem malesuada magna mollis euismod. Nulla vitae elit libero, a pharetra augue.</p>
  </div>
</footer>
<div class="copyright">© 2015 Kelva. All rights reserved.</div>

</body>
</html>
```